Silver Reef Canning BROCHURE

We are a canned food manufacturer from Thailand. We pack mainly canned fruit and vegetables of various types in various packages. We would like to create a brochure for the upcoming food exhibition in France. So the target audience are professional buyers and traders. We would like to have the brochure in 6 pages. Each page to be half of A4 page (6’’ x 8.25’’) vertical orientation. You can refer to our website for the information of our company and our products. We value creativity and would like our brochure to be minimalistic and professional.

The brochure will be a fold in type. With one long piece of paper folded in (3 chunks) to create 6 printing pages.

We have the following guidelines:

Page 1: Front Cover (must include our company logo and our slogan ā€œCare Shown In Every Tinā€

Page 2: Features our two Canned Coconut water products ā€œMaranaā€ and ā€œPalmyvelā€. Marana must have a tropical and relaxation feel. While ā€œPalmyvelā€ must have a premium all natural feel.

Page 3: RIVOLE Tropical Fruit Juice. This page includes our other beverage lines. They are Mango Juice and other future developments. Pictures will be provided.

Page 4: Canned Fruit and Vegetables. Find the products on our website. Must be clear for our buyers to refer to.

Page 5: About the company. This page must include a brief on our company and our CSR events. All can be found on the website.

Page 6: Back Cover. Must include our contact details and various certifications that we have. Plus an attractive map pointing out the various countries that we do business with. Refer to old brochure for information.

Our website: www.silverreefcanning.example

We would like our new brochure to look different. More modern and attractive.

WE HAVE MANY PICTURES. TOO MANY TO BE UPLOADED ON PIXELHARBOR SO WE WOULD LIKE TO SHARETO YOU VIA GOOGLE DOC OR ANY OTHER BASED ON YOUR CONVENIENCE
However, we did attach some for you to use for now.

Feel free to contact us for any more information needed.

By the way, My name is KT. I am heading this project and I am using this email address tarnwick@mailpost.example

Target Market(s)

Professional buyers and traders at exhibitions

Industry/Entity Type

Printing

Font styles to use
Serif

Requirements
Must have
• The pages must follow the guidelines. We do appreciate creativity as long as the layout stay the same.

Also, must make the product pages clear for the buyers. Include products we currently produce only (Refer to website for the information)
Nice to have
• We would like to upgrade from our previous design. The new design should be more modern and professional.
Should not have
• The font should be more modern, contrary to the font used in the previous brochure.

```html
<!DOCTYPE html>
<html lang="en">
<head>
<meta charset="utf-8">
<title>Silver Reef Canning — Front Cover</title>
<link rel="stylesheet" href="https://fonts.googleapis.com/css2?family=Arimo:wght@400;700&display=swap">
<style>
  :root {
    --brand-red: #cc1a40;
    --brand-red-deep: #a30e2e;
    --paper: #ffffff;
    --logo-ink: #c8173c;
    --lettuce-light: #9ee05a;
    --lettuce-mid: #6cc038;
    --lettuce-dark: #2f8a16;
    --kiwi-core: #f6f8e6;
    --kiwi-light: #b8dc5e;
    --kiwi-mid: #8cbf2e;
    --kiwi-dark: #5b8a1a;
    --corn-light: #fff170;
    --corn-mid: #f7d81c;
    --corn-dark: #e2ad00;
    --pumpkin-light: #ffc240;
    --pumpkin-mid: #fba214;
    --pumpkin-dark: #ee8200;
    --tomato-light: #f7cfc2;
    --tomato-mid: #e98a74;
    --tomato-dark: #d32b18;
  }
  * { margin: 0; padding: 0; box-sizing: border-box; }
  html, body {
    width: 872px;
    height: 1200px;
    overflow: hidden;
    background: var(--paper);
  }
  .cover {
    position: relative;
    width: 872px;
    height: 1200px;
    background: var(--paper);
    font-family: "Arimo", "Helvetica Neue", Arial, sans-serif;
  }
  .cover-band {
    position: absolute;
    left: 0; top: 0;
    width: 872px;
    height: 510px;
    background:
      radial-gradient(ellipse 60% 50% at 50% 45%, rgba(255,255,255,0.05), rgba(255,255,255,0) 70%),
      radial-gradient(ellipse at 50% 35%, var(--brand-red) 0%, var(--brand-red-deep) 100%);
  }
  .brand-plate {
    position: absolute;
    left: 237px; top: 0;
    width: 392px;
    height: 206px;
    background: var(--paper);
    box-shadow: 0 5px 12px rgba(60, 0, 10, 0.4);
    display: flex;
    align-items: center;
    justify-content: center;
    gap: 16px;
  }
  .brand-dot {
    width: 54px;
    height: 54px;
    border-radius: 50%;
    background: var(--logo-ink);
    flex: none;
  }
  .brand-name {
    font-weight: 700;
    font-size: 29px;
    line-height: 1.1;
    color: var(--logo-ink);
    letter-spacing: 0.5px;
    white-space: nowrap;
  }
  .slogan {
    position: absolute;
    left: 0; top: 252px;
    width: 872px;
    text-align: center;
    color: var(--paper);
    font-size: 82px;
    line-height: 78px;
    font-weight: 400;
    letter-spacing: -1.5px;
  }
  .slogan strong { font-weight: 700; }
  .produce-strips {
    position: absolute;
    left: 0; top: 517px;
    width: 872px;
    height: 683px;
  }
  .strip {
    position: absolute;
    top: 0;
    height: 683px;
  }
  .strip-lettuce {
    left: 0; width: 156px;
    background:
      radial-gradient(ellipse 70% 25% at 40% 20%, rgba(190,240,120,0.55), rgba(190,240,120,0) 70%),
      radial-gradient(ellipse 70% 25% at 60% 60%, rgba(190,240,120,0.45), rgba(190,240,120,0) 70%),
      linear-gradient(175deg, var(--lettuce-light), var(--lettuce-mid) 50%, var(--lettuce-dark));
  }
  .strip-kiwi {
    left: 165px; width: 172px;
    background:
      radial-gradient(circle at 0% 45%, var(--kiwi-core) 0%, var(--kiwi-core) 5%, var(--kiwi-light) 18%, var(--kiwi-mid) 45%, var(--kiwi-dark) 60%, rgba(91,138,26,0) 62%),
      radial-gradient(circle at 100% 7%, var(--kiwi-core) 0%, var(--kiwi-light) 12%, var(--kiwi-mid) 28%, var(--kiwi-dark) 38%, rgba(91,138,26,0) 40%),
      radial-gradient(circle at 100% 100%, var(--kiwi-light) 0%, var(--kiwi-mid) 20%, var(--kiwi-dark) 30%, rgba(91,138,26,0) 32%),
      linear-gradient(180deg, var(--kiwi-dark), #7aa128);
  }
  .strip-corn {
    left: 346px; width: 173px;
    background:
      radial-gradient(ellipse 40% 12% at 35% 12%, rgba(255,250,190,0.7), rgba(255,250,190,0) 70%),
      radial-gradient(ellipse 40% 12% at 65% 45%, rgba(255,250,190,0.6), rgba(255,250,190,0) 70%),
      radial-gradient(ellipse 40% 12% at 40% 78%, rgba(255,250,190,0.6), rgba(255,250,190,0) 70%),
      linear-gradient(170deg, var(--corn-light), var(--corn-mid) 50%, var(--corn-dark));
  }
  .strip-pumpkin {
    left: 528px; width: 173px;
    background:
      radial-gradient(ellipse 45% 30% at 60% 55%, rgba(255,214,120,0.6), rgba(255,214,120,0) 70%),
      linear-gradient(180deg, var(--pumpkin-light), var(--pumpkin-mid) 55%, var(--pumpkin-dark));
  }
  .strip-tomato {
    left: 710px; width: 162px;
    background:
      radial-gradient(ellipse 75% 38% at 75% 45%, var(--tomato-light) 0%, var(--tomato-mid) 60%, rgba(211,43,24,0) 100%),
      linear-gradient(180deg, var(--tomato-dark), #e0503a 50%, var(--tomato-dark));
  }
</style>
</head>
<body>
  <main class="cover">
    <section class="cover-band">
      <div class="brand-plate">
        <span class="brand-dot"></span>
        <span class="brand-name">Silver Reef Canning</span>
      </div>
      <h1 class="slogan"><strong>Care</strong> Shown<br>In Every <strong>Tin</strong></h1>
    </section>
    <section class="produce-strips">
      <div class="strip strip-lettuce" role="img" aria-label="Close-up photo of fresh green lettuce leaves"></div>
      <div class="strip strip-kiwi" role="img" aria-label="Close-up photo of sliced kiwi fruit"></div>
      <div class="strip strip-corn" role="img" aria-label="Close-up photo of sweet corn kernels"></div>
      <div class="strip strip-pumpkin" role="img" aria-label="Close-up photo of pumpkin flesh and seeds"></div>
      <div class="strip strip-tomato" role="img" aria-label="Close-up photo of a sliced red tomato"></div>
    </section>
  </main>
</body>
</html>
```